Amber Reed Catering Menu

Design 1 page (double sided is ok) menu for catering company.

A flat non-folding menu. Letter paper sized.
Updates

I'm having trouble adding attachments via Pixel Forum.  I have contacted Pixel Forum and will hopefully have them up soon.  

Industry/Entity Type

Catering

Font styles to use
Serif

Requirements
Must have
• Amber Reed Catering logo

menu items from attachment

Double sided is ok

```html
<!DOCTYPE html>
<html lang="en">
<head>
<meta charset="utf-8">
<title>Amber Reed Catering Menu</title>
<link href="https://fonts.googleapis.com/css2?family=Cinzel:wght@400;600&family=Tinos:ital,wght@0,400;0,700;1,400&display=swap" rel="stylesheet">
<style>
:root{
  --blue:#2fa3d8;
  --sky:#5cc3ea;
  --green:#78be43;
  --ink:#1d1d1d;
  --paper:#ffffff;
  --wash-a:#d7eef8;
  --wash-b:#e4f2d8;
}
*{box-sizing:border-box;margin:0;padding:0}
html,body{width:1200px;height:928px;overflow:hidden;background:var(--paper)}
body{font-family:"Tinos","Times New Roman",serif;color:var(--ink);position:relative}
.frame{position:absolute;inset:6px;border:3px solid var(--sky);}
.frame::after{content:"";position:absolute;inset:4px;border:1px solid var(--sky)}
.vrule{position:absolute;top:40px;bottom:30px;border-left:1px dotted var(--blue)}
.hrule{position:absolute;height:0;border-top:1px dotted var(--blue)}
.block{position:absolute;text-align:center}
.brand{font-family:"Cinzel",serif;font-weight:400;color:var(--blue);font-size:29px;letter-spacing:.5px;line-height:1;white-space:nowrap}
.director{font-family:"Cinzel",serif;font-size:16px;letter-spacing:.5px}
.director-name{font-size:24px;margin-top:4px}
.contacts{list-style:none;text-align:left;margin:12px auto 0;width:200px}
.contacts li{display:flex;align-items:center;font-size:22px;height:38px}
.contacts .dot{width:20px;height:20px;border-radius:50%;background:var(--blue);color:#fff;font-size:11px;font-weight:700;display:flex;align-items:center;justify-content:center;margin-right:14px}
.feature-area{position:absolute;left:142px;top:410px;width:158px;height:130px;border-radius:6px;background:linear-gradient(160deg,var(--wash-a),var(--wash-b))}
.tagline{font-style:italic;font-size:23px;line-height:30px}
.sep{color:var(--blue);font-size:15px;margin:4px 0 6px;font-style:normal}
.icon{display:block;margin:0 auto;background:var(--sky);border-radius:12px 12px 4px 4px}
.heading{font-family:"Cinzel",serif;font-weight:600;color:var(--green);font-size:25px;margin:12px 0 12px}
.item{font-size:14.5px;line-height:20px;margin-bottom:16px}
.item b{display:block;font-weight:700}
.item i{display:block}
.lunch .item{margin-bottom:12px}
.specialty{font-weight:700;font-size:14.5px;margin-bottom:14px}
.sub{font-weight:700;font-size:14.5px;display:block}
.note{font-size:14px;line-height:20px}
</style>
</head>
<body>
<div class="frame"></div>
<div class="vrule" style="left:411px"></div>
<div class="vrule" style="left:789px"></div>
<div class="hrule" style="left:42px;width:358px;top:388px"></div>
<div class="hrule" style="left:422px;width:356px;top:554px"></div>
<div class="hrule" style="left:800px;width:358px;top:612px"></div>

<section class="block" style="left:42px;top:84px;width:358px">
  <div class="brand">Amber Reed Catering</div>
</section>

<section class="block" style="left:42px;top:176px;width:358px">
  <div class="director">Catering Director</div>
  <div class="director-name">Dana Whitlock</div>
  <ul class="contacts">
    <li><span class="dot">T</span>555-214-3905</li>
    <li><span class="dot">F</span>555-214-1939</li>
    <li><span class="dot">M</span>555-738-0141</li>
  </ul>
</section>

<div class="feature-area" role="img" aria-label="Business emblem area"></div>

<section class="block" style="left:42px;top:580px;width:358px">
  <p class="tagline">Caterings for all occasions</p>
  <p class="sep">✦</p>
  <p class="tagline">Enjoy our pre-set menu or<br>we can customize something<br>more personal for you</p>
  <p class="sep">✦</p>
  <p class="tagline">Set up and delivery is included<br>in all prices listed</p>
  <p class="sep">✦</p>
</section>

<section class="block" style="left:422px;top:56px;width:356px">
  <span class="icon" role="img" aria-label="Serving cloche icon" style="width:64px;height:30px;border-radius:32px 32px 3px 3px"></span>
  <h2 class="heading">Breakfast</h2>
  <div class="item"><b>Morning Stretch $5.99 per guest</b><i>Assorted Danishes, Muffins, Bagels with<br>Cream Cheese, Butter, Jelly<br>Fresh Brewed Coffee, Decaf and Assorted Teas</i></div>
  <div class="item"><b>Healthy Start $6.99 per guest</b><i>Fresh Fruit, Assorted Muffins or<br>Bagels with Cream Cheese, Butter, Jelly<br>Fresh Brewed Coffee, Decaf and Assorted Teas<br>Orange Juice</i></div>
  <div class="item"><b>Breakfast Sandwich $7.99 per guest</b><i>Bagel, Biscuit or Wrap with Egg and Cheese<br>with choice of: Bacon, Sausage or Ham<br>Fresh Brewed Coffee Decaf and Assorted Teas<br>Orange Juice</i></div>
  <div class="item"><b>Grand Deluxe $8.99 per guest</b><i>Fresh Scrambled Eggs, Bacon, Home Fries, Bread<br>Fresh Brewed Coffee, Decaf and Assorted Tea<br>Orange Juice</i></div>
</section>

<section class="block lunch" style="left:422px;top:570px;width:356px">
  <span class="icon" role="img" aria-label="Cooking pot icon" style="width:48px;height:38px"></span>
  <h2 class="heading">Lunch</h2>
  <div class="item"><b>Boxed Lunch $7.99 per guest</b><i>Sandwich or Wrap with choice of:<br>Assorted Chips, Pasta Salad, or Potato Salad<br>Brownie or Cookie<br>Can Soda or Bottle Water</i></div>
  <div class="item"><b>Cold Cut Platter $9.99 per guest</b><i>Assorted Meats (Turkey, Ham, Roast Beef)<br>and Cheeses with varying Breads and choice of:<br>Potato Salad, Pasta Salad, Coleslaw, or Chips<br>Cookie or Brownie<br>Can Soda or Bottle Water</i></div>
</section>

<section class="block" style="left:800px;top:56px;width:358px">
  <span class="icon" role="img" aria-label="Sandwich icon" style="width:36px;height:32px;border-radius:8px"></span>
  <h2 class="heading">Sandwiches</h2>
  <p class="specialty">Specialty Sandwich $6.99 per guest</p>
  <div class="item"><span class="sub">ITALIAN WRAP</span><i>Salami, Pepperoni, Ham and Cheese Lettuce Tomato<br>with Italian Dressing</i></div>
  <div class="item"><span class="sub">SOUTHWEST STEAK WRAP</span><i>Steak, Roasted Red Peppers, Lettuce Cheese<br>with Southwest Dressing</i></div>
  <div class="item"><span class="sub">THE HIGHLANDER</span><i>Smoked Turkey, Alpine Cheese, Tomatoes,<br>Lettuce Honey Dijon with Sourdough Bread</i></div>
  <div class="item"><span class="sub">GRILLED VEGETARIAN</span><i>Grilled Veggies with Lettuce,<br>Tomato Balsamic Vinaigrette<br>Wrapper or Bread</i></div>
  <div class="item"><span class="sub">THE TRADITIONAL</span><i>Roast Beef, Lettuce, Tomatoes,<br>Horseradish Mayonnaise On a Roll</i></div>
  <p class="note">* Custom Foot Long Subs Available by Request<br>$13.99 per foot</p>
</section>

<section class="block" style="left:800px;top:648px;width:358px">
  <span class="icon" role="img" aria-label="Salad platter icon" style="width:110px;height:42px;border-radius:40px 40px 6px 6px"></span>
  <h2 class="heading">Salads</h2>
  <div class="item"><b>GREEK SALAD $8.99 per guest</b><i>Mixed Greens, Green Peppers, Kalamato Olives,<br>Feta Cheese, Tomatoes, Greek Peppers Greek Dressing</i></div>
  <div class="item"><b>GRILLED CHICKEN SALAD $9.99 per guest</b><i>Grilled Chicken, Roquefort Cheese, and Walnuts with<br>Mixed Greens Balsamic Dressing</i></div>
</section>
</body>
</html>
```